Velvora VIP Golden Ticket postcard design

Velvora is a new massage parlour opening in Manchester England this is a second business for me and I want to create a post card size VIP Golden ticket for our regular customers offering a free glass of champagne with there first service and a discounted rate for the first month it needs to incorporate the address 217b Hensley Vale Road Chorlton Manchester M21 4QT, telephone number 0161-493-2586.The website address www.Velvorrasuite.example.co.uk. I want the post card to be gold with the name Velvora in pink the rest of the wording in black where it says free glass of champagne the text needs to be bold. The overall look of the post ccad should communicate glamour and luxury with style and finesse

```html
<!DOCTYPE html>
<html lang="en">
<head>
<meta charset="utf-8">
<title>Velvora VIP Golden Ticket</title>
<link rel="stylesheet" href="https://fonts.googleapis.com/css2?family=Oswald:wght@700&family=Yellowtail&family=Signika:wght@400;600;700&display=swap">
<style>
  :root {
    --gold-deep: #8a5a0c;
    --gold-mid: #c8951f;
    --gold-light: #f3dc74;
    --gold-pale: #fbf0a6;
    --olive-gold: #9c8414;
    --bar-black: #111008;
    --pink: #ff2bd0;
    --pink-shade: #8a0f6a;
    --rule-yellow: #f5ea3c;
    --ink: #111111;
  }
  html, body {
    margin: 0;
    padding: 0;
    width: 1200px;
    height: 930px;
    overflow: hidden;
    background: #ffffff;
  }
  .ticket {
    position: relative;
    width: 1200px;
    height: 930px;
    overflow: hidden;
    font-family: "Signika", sans-serif;
    background: linear-gradient(90deg,
      var(--olive-gold) 0%,
      var(--gold-light) 3%,
      var(--gold-mid) 6.8%,
      var(--gold-deep) 7%,
      var(--gold-mid) 25%,
      var(--gold-light) 50%,
      var(--gold-mid) 75%,
      var(--gold-deep) 93%,
      var(--gold-mid) 93.2%,
      var(--gold-light) 97%,
      var(--olive-gold) 100%);
  }
  .ticket__glow {
    position: absolute;
    left: 82px;
    right: 82px;
    top: 0;
    bottom: 0;
    background:
      radial-gradient(ellipse 60% 45% at 50% 40%, rgba(255, 244, 170, 0.55), rgba(255, 244, 170, 0) 70%),
      linear-gradient(180deg, rgba(120, 70, 0, 0.25) 0%, rgba(255, 240, 150, 0.15) 45%, rgba(255, 250, 190, 0.45) 100%);
  }
  .ticket__bar {
    position: absolute;
    top: 84px;
    height: 28px;
    background: var(--bar-black);
  }
  .ticket__bar--left { left: 0; width: 462px; }
  .ticket__bar--right { left: 741px; right: 0; }
  .ticket__vip {
    position: absolute;
    top: 10px;
    left: 0;
    width: 100%;
    text-align: center;
    font-family: "Oswald", sans-serif;
    font-weight: 700;
    font-size: 170px;
    line-height: 1;
    letter-spacing: -2px;
    background: linear-gradient(180deg, #fffbe0 0%, #f6d86a 35%, #9a5a06 55%, #d9a53a 75%, #6b3d02 100%);
    -webkit-background-clip: text;
    background-clip: text;
    color: transparent;
    filter: drop-shadow(2px 3px 2px rgba(60, 30, 0, 0.5));
  }
  .ticket__name {
    position: absolute;
    top: 175px;
    left: 0;
    width: 100%;
    text-align: center;
    font-family: "Yellowtail", cursive;
    font-size: 250px;
    line-height: 1.1;
    color: var(--pink);
    text-shadow: 3px 4px 0 var(--pink-shade);
  }
  .ticket__rule {
    position: absolute;
    left: 215px;
    width: 772px;
    height: 6px;
    background: var(--rule-yellow);
    box-shadow: 0 2px 0 rgba(110, 70, 0, 0.6);
  }
  .ticket__rule--top { top: 550px; }
  .ticket__rule--bottom { top: 728px; }
  .ticket__offer {
    position: absolute;
    top: 582px;
    left: 0;
    width: 100%;
    margin: 0;
    text-align: center;
    color: var(--ink);
    font-size: 27px;
    font-weight: 600;
    line-height: 42px;
    letter-spacing: 0.5px;
    text-transform: uppercase;
  }
  .ticket__offer strong { font-weight: 700; }
  .ticket__contact {
    position: absolute;
    top: 776px;
    left: 0;
    width: 100%;
    margin: 0;
    font-style: normal;
    text-align: center;
    color: var(--ink);
    font-size: 19px;
    font-weight: 600;
    line-height: 30px;
  }
</style>
</head>
<body>
  <main class="ticket">
    <div class="ticket__glow"></div>
    <div class="ticket__bar ticket__bar--left"></div>
    <div class="ticket__bar ticket__bar--right"></div>
    <div class="ticket__vip">VIP</div>
    <h1 class="ticket__name" style="margin:0;font-weight:400;">Velvora</h1>
    <div class="ticket__rule ticket__rule--top"></div>
    <p class="ticket__offer">
      <strong>Free glass of champange with your first purchase</strong><br>
      *Plus*<br>
      A discounted rate for the first month
    </p>
    <div class="ticket__rule ticket__rule--bottom"></div>
    <address class="ticket__contact">
      217b Hensley Vale Road Chorlton Manchester M21 4QT<br>
      0161-493-2586.<br>
      www.Velvorrasuite.example.co.uk
    </address>
  </main>
</body>
</html>
```